依頼概要
初めまして。本書は、会社等の会議を実施する立場の人に向けてのものと
なっております。
■依頼の目的/概要
lumora出版、ビジネスパーソン向け書籍の表紙デザインをお願いします。
今のところ、題名は
「だれでも週末から家庭菜園がはかどる」

■本の内容
会社等で、会議をうまく進めていきたいがなかなか思うように
薦められない方向けに、誰でも簡単にこれだけのことを実践すれば
会議が上手く進められるというポイントをまとめたものになっております。

■デザイン要望
ビジネスパーソン向けですが、会議等に不慣れな方向けで
あまり難しく考えなくても、誰でも簡単にトライできるという
イメージを持ってもらえるようにしたいです。

現在、原稿は9割がたできております。添付ファイルをご参照ください。

その他何かご不明な点がございましたら、お気軽にご質問下さい。
よろしくお願いいたします。
名前は、ペンネームにする予定です。
今のところ、柚木 瑛之助が候補です。
■ 選んだ理由

私のイメージする会社内での和気あいあいとした雰囲気のイラストがまずは
気に入りました。
ターゲットが、会議がうまくできない人向けなので、なるべくそれを意識して
親しみやすいものを選びました。

■ 提案者全員のお礼・コメント

今回は、ターゲットが初心者向けであったので、親しみやすいものを選びましたが、
例えば、会議を上から見たイラストなどは、斬新なアイデアで印象深く
ターゲットが違えば、選んでいたと思います。
中身を理解して、提案いただけた方も多く、感謝いたします。
今後も、このシリーズを出版していきたいと考えておりますので
次の機会もよろしくお願いいたします。
ありがとうございました。

```html
<!DOCTYPE html>
<html lang="ja">
<head>
<meta charset="utf-8">
<title>だれでも週末から家庭菜園がはかどる</title>
<link rel="stylesheet" href="https://fonts.googleapis.com/css2?family=M+PLUS+Rounded+1c:wght@800;900&family=Noto+Sans+JP:wght@700;900&display=swap">
<style>
  :root {
    --green: #2f9a3a;
    --green-deep: #1f6d2a;
    --red: #e5322a;
    --yellow: #ffe600;
    --ink: #333333;
    --paper: #ffffff;
    --bubble-edge: #2f9a3a;
  }
  * { margin: 0; padding: 0; box-sizing: border-box; }
  html, body { width: 750px; height: 1200px; overflow: hidden; background: var(--paper); }
  .cover {
    position: relative; width: 750px; height: 1200px; overflow: hidden;
    background: var(--paper);
    font-family: "Noto Sans JP", sans-serif;
  }
  .title-lead {
    position: absolute; top: 14px; left: 0; width: 100%;
    text-align: center;
    font-family: "M PLUS Rounded 1c", sans-serif; font-weight: 900;
    font-size: 60px; color: var(--green); letter-spacing: 2px;
  }
  .title-lead .accent { color: var(--red); }
  .hero-figure {
    position: absolute; left: 268px; top: 110px; width: 230px; height: 600px;
    border-radius: 110px 110px 20px 20px;
    background: linear-gradient(180deg, #3b3b45 0%, #f2d2b6 18%, #6d7f96 40%, #55667d 100%);
    opacity: .9;
  }
  .title-big {
    position: absolute;
    font-family: "M PLUS Rounded 1c", sans-serif; font-weight: 900;
    color: var(--green); line-height: 1;
    -webkit-text-stroke: 6px var(--paper); paint-order: stroke fill;
  }
  .title-big.left { left: 48px; top: 120px; font-size: 150px; }
  .title-big.right { right: 48px; top: 120px; font-size: 150px; }
  .title-big span { display: block; margin-bottom: 6px; }
  .title-particle {
    position: absolute; right: 260px; top: 430px;
    font-family: "M PLUS Rounded 1c", sans-serif; font-weight: 900;
    font-size: 78px; color: var(--red);
    -webkit-text-stroke: 6px var(--paper); paint-order: stroke fill;
  }
  .title-tail {
    position: absolute; left: 0; top: 510px; width: 100%; text-align: center;
    font-family: "M PLUS Rounded 1c", sans-serif; font-weight: 900;
    font-size: 138px; color: var(--red); line-height: 1; letter-spacing: 10px;
    -webkit-text-stroke: 8px var(--paper); paint-order: stroke fill;
  }
  .author {
    position: absolute; right: 40px; top: 660px;
    font-weight: 700; font-size: 30px; color: var(--ink); letter-spacing: 2px;
  }
  .author small { font-size: 22px; margin-left: 8px; }
  .promo {
    position: absolute; left: 0; top: 712px; width: 750px; height: 488px;
    background: var(--green);
  }
  .promo-copy {
    position: absolute; left: 40px; top: 22px;
    font-weight: 900; font-size: 35px; line-height: 1.45; color: var(--paper);
  }
  .promo-copy .hl { color: var(--yellow); }
  .checklist { position: absolute; left: 40px; top: 150px; list-style: none; }
  .checklist li {
    display: flex; align-items: center; gap: 12px; margin-bottom: 22px;
    background: var(--paper); padding: 6px 24px 6px 14px; border-radius: 6px;
    font-weight: 900; font-size: 44px; color: var(--red); width: max-content;
  }
  .checklist svg { width: 52px; height: 52px; }
  .speech {
    position: absolute; left: 488px; top: 100px; width: 170px; height: 140px;
    background: var(--paper); border: 3px solid var(--bubble-edge); border-radius: 50%;
    display: flex; align-items: center; justify-content: center; text-align: center;
    font-weight: 700; font-size: 17px; line-height: 1.35; color: var(--ink);
  }
  .guide-figure {
    position: absolute; left: 520px; top: 245px; width: 200px; height: 175px;
    border-radius: 90px 90px 10px 10px;
    background: linear-gradient(180deg, #3b3b45 0%, #f2d2b6 30%, #5c6e86 70%);
  }
  .closing {
    position: absolute; left: 0; bottom: 0; width: 750px; height: 80px;
    background: var(--green-deep);
    display: flex; align-items: center; justify-content: center;
    font-weight: 900; font-size: 48px; color: var(--paper); letter-spacing: 2px;
  }
</style>
</head>
<body>
<main class="cover">
  <h1 class="title-lead">だれでも<span class="accent">週末</span>から</h1>

  <div class="hero-figure" role="img" aria-label="ガッツポーズをするスーツ姿の男性のイラスト"></div>

  <div class="title-big left"><span>家</span><span>庭</span></div>
  <div class="title-big right"><span>菜</span><span>園</span></div>
  <div class="title-particle">が</div>
  <div class="title-tail">はかどる</div>

  <p class="author">柚木 瑛之助<small>著</small></p>

  <section class="promo">
    <p class="promo-copy">誰でも<span class="hl">比較的簡単</span>に会議ができる<br>ポイントを集約しました。</p>

    <ul class="checklist">
      <li>
        <svg viewBox="0 0 52 52" aria-hidden="true"><rect x="4" y="8" width="38" height="38" fill="none" stroke="#e5322a" stroke-width="5"/><path d="M12 26 L22 38 L46 6" fill="none" stroke="#e5322a" stroke-width="7" stroke-linecap="round" stroke-linejoin="round"/></svg>
        進行表
      </li>
      <li>
        <svg viewBox="0 0 52 52" aria-hidden="true"><rect x="4" y="8" width="38" height="38" fill="none" stroke="#e5322a" stroke-width="5"/><path d="M12 26 L22 38 L46 6" fill="none" stroke="#e5322a" stroke-width="7" stroke-linecap="round" stroke-linejoin="round"/></svg>
        終了条件
      </li>
    </ul>

    <div class="speech">慣れてしまえば、<br>時間や手間を<br>かけなくても<br>大丈夫です！</div>
    <div class="guide-figure" role="img" aria-label="資料を手に説明する男性のイラスト"></div>

    <p class="closing">これだけ準備すれば大丈夫</p>
  </section>
</main>
</body>
</html>
```